Business Card and Letterhead for Juniper Anvil - (Have Logo)

Update 4: Removed company reg no from business card details as it looked a bit out of place. Updated services list.
UPDATE 3
Sorry, I got the address a little bit wrong, have updated it below. Sorry for any inconvenience caused.
UPDATE 2
Finally I have the details for the business cards and letterhead. Submissions already made do not have to be updated unless shortlisted, if all new submissions could include the details for me, Marcus, that would be very much appreciated and help with the final shortlist selection. I intend to share a shortlist of the three best entries with past and existing customers for their feedback and opinions. Thank you all again for your time.
Here are the details.
Marcus Telby
Web Developer
T: 01632 960 418
E: marcus@juniperanvil.example
www.juniperanvil.example
Professional Photography
Web Solutions & E-Commerce
Audio & HD Video Production
Marketing & Promotions
Identity and Branding
Juniper Anvil Ltd
Suite 20938, 3rd Floor
212-224 Orchard Lane
London, N7 9QX
Company Reg. No: 05829147
The order and the layout of the information are of course down to the design, but the company registration number should be smaller and less prominent. The formatting of the telephone and email address using a T: and an E: I am not sure about and again if it is Tel: or Email: or Icons is up to the design.
The Company No. on the letterhead should read (somewhere in small text along the bottom):
Juniper Anvil is a Ltd Company registered in England & Wales, Registration No. 05829147.
The second business card details are
Oliver Brackley
Photographer
T: 01632 960 418
E: oliver@juniperanvil.example
Everything else the same of course.
Thank you again for all the submissions so far.
END OF UPDATE 2
-
UPDATE 1: Please do not alter the logo nor the logo colours. (This was a previous pixel forum project and I am extremely happy with it. The icon can stand alone of course, but I have had to eliminate all entries that have made it black and white, or reversed the icon.) I would like to thank everyone that has participated so far and am very grateful for all your thought and time.
End of Update 1
-
Original Brief:
I have attached the logo vector file.
Following a superb logo from a previous Pixel Forum project I am now looking for a business card design and (although less important) a letterhead as well.
I must admit I tried to do it myself but could only come up with the usual amateur stuff that in comparison to the quality of the logo looked awful.
About Us
Juniper Anvil Ltd will be a new company due to start in January. It is really just me (a web developer) and my friend (a photographer). We will be aiming at the usual small to medium sized businesses in the local area, selling various digital services including photographic services to the public, web hosting and development, commercial photography, modelling services (not us!), full video and film production and possibly a bit of marketing as well. (Really it is anything we can do professionally all lumped together! We met running seperate businesses which have both since closed)
We will not be competing on price. We plan to be expensive but fair. Certainly not the cheapest.
What we are looking for
Business Card
I imagine a double sided business card, which will be used for more than one person. I imagine the front to be the same for everyone and the persons details to be on the back, although this is of course only my thoughts and I am of course completely open to any ideas.
The card could also have a services list or a bit about what we do on it. It might feature the website address, our business address (mail forwarding address) or our registered company number.
Or it might have none of that, we are completely open to any ideas and have no real fixed opinions. I just want it to be really nice :-)
Letterhead (secondary importance)
We will make our decision primarily on the business card, although a mathcing letterhead would be fantastic. Something standardish in format and simple, although again, all ideas are welcomed.
I hope that is enough information but if you have any questions I will answer them as fully and as quickly as possible.
Thank you once again and I really look forward to seeing your ideas and picking a winner.
Marcus T.
Small businesses AND the general public
Film Production

```html
<!DOCTYPE html>
<html lang="en">
<head>
<meta charset="utf-8">
<title>Juniper Anvil – Stationery</title>
<link href="https://fonts.googleapis.com/css2?family=Open+Sans:ital,wght@0,400;0,700;1,400&display=swap" rel="stylesheet">
<style>
:root{
  --board:#c9cacc;
  --paper:#ffffff;
  --brand-red:#b5121b;
  --charcoal:#58595b;
  --charcoal-dark:#4a4a4c;
  --text-grey:#9a9a9c;
  --text-dark:#3c3c3e;
  --panel-grey:#e6e6e7;
}
*{box-sizing:border-box;margin:0;padding:0}
html,body{width:1200px;height:1114px;overflow:hidden}
body{background:var(--board);font-family:"Open Sans",Arial,sans-serif;position:relative}

.wordmark{display:flex;align-items:center;gap:8px;white-space:nowrap}
.wordmark .mark-square{flex:none;background:var(--brand-red)}
.wordmark .name{font-weight:700;color:var(--brand-red);text-transform:uppercase;line-height:1}
address{font-style:normal}

/* Letterhead */
.letterhead{position:absolute;left:96px;top:60px;width:730px;height:1034px;background:var(--paper)}
.letterhead .services{position:absolute;left:50px;top:22px;list-style:none;font-size:12px;line-height:15px;color:var(--text-grey)}
.letterhead .wordmark{position:absolute;left:276px;top:30px}
.letterhead .wordmark .mark-square{width:24px;height:24px}
.letterhead .wordmark .name{font-size:22px}
.letterhead .address{position:absolute;left:560px;top:22px;font-size:12px;line-height:15px;color:var(--text-grey)}
.letterhead .side-panel{position:absolute;left:0;top:906px;width:318px;height:66px;background:var(--panel-grey)}
.letterhead .footer-band{position:absolute;left:0;bottom:0;width:100%;height:62px;background:var(--brand-red);color:#fff;font-size:11px;display:flex;align-items:center;justify-content:center}

/* Business cards */
.card{position:absolute;border-radius:10px;overflow:hidden}
.card-front{left:856px;top:60px;width:312px;height:182px;background:var(--charcoal)}
.card-front .address{position:absolute;right:12px;top:10px;text-align:right;font-size:8px;line-height:10px;color:#fff}
.card-front .wordmark{position:absolute;right:14px;top:72px;gap:6px}
.card-front .wordmark .mark-square{width:18px;height:18px}
.card-front .wordmark .name{font-size:17px}
.card-front .services{position:absolute;left:92px;top:140px;list-style:none;font-size:7.5px;line-height:10px;color:#fff;white-space:nowrap}

.card-back{left:848px;top:264px;width:320px;height:180px;background:var(--paper)}
.card-back .wordmark{position:absolute;left:14px;top:20px;gap:6px}
.card-back .wordmark .mark-square{width:18px;height:18px}
.card-back .wordmark .name{font-size:16px}
.card-back .details{position:absolute;left:14px;top:74px;font-size:9.5px;line-height:13px;color:var(--text-dark)}
.details .role{color:var(--brand-red);font-style:italic;margin-bottom:6px}
.details .web{color:var(--brand-red);margin-top:6px}
.details .reg{font-size:8.5px}
.card-back .corner-block{position:absolute;left:186px;top:146px;width:122px;height:34px;background:var(--charcoal-dark)}
</style>
</head>
<body>

<section class="letterhead">
  <ul class="services">
    <li>Professional Photography</li>
    <li>Web Solutions &amp; E-Commerce</li>
    <li>Audio &amp; HD Video Production</li>
    <li>Marketing &amp; Promotions</li>
    <li>Identity and Branding</li>
  </ul>
  <div class="wordmark"><span class="mark-square"></span><span class="name">Juniper Anvil</span></div>
  <address class="address">
    Juniper Anvil Ltd<br>
    Suite 20938, 3rd Floor<br>
    212-224 Orchard Lane<br>
    London, N7 9QX
  </address>
  <div class="side-panel"></div>
  <footer class="footer-band">Juniper Anvil is a Ltd Company registered in England &amp; Wales. Registration No. 05829147.</footer>
</section>

<section class="card card-front">
  <address class="address">
    Juniper Anvil Ltd<br>
    Suite 20938, 3rd Floor<br>
    212-224 Orchard Lane<br>
    London, N7 9QX
  </address>
  <div class="wordmark"><span class="mark-square"></span><span class="name">Juniper Anvil</span></div>
  <ul class="services">
    <li>Professional Photography · Web Solutions &amp; E-Commerce</li>
    <li>Audio &amp; HD Video Production · Marketing &amp; Promotions</li>
    <li>Identity and Branding</li>
  </ul>
</section>

<section class="card card-back">
  <div class="wordmark"><span class="mark-square"></span><span class="name">Juniper Anvil</span></div>
  <div class="details">
    <p class="person">Marcus Telby</p>
    <p class="role">Web Developer</p>
    <p>T: 01632 960 418</p>
    <p>E: marcus@juniperanvil.example</p>
    <p class="web">www.juniperanvil.example</p>
    <p class="reg">Company Reg. No: 05829147</p>
  </div>
  <div class="corner-block"></div>
</section>

</body>
</html>
```